Website improvements and Adding Functionalities at https://quorin.net/tamberly

1.Search functionality
2.Payment process functionality
3. Application configuration
4. Registration functionality activation
5. Chat functionality
6.Language switching functionality (Portuguese & French)
7.Bespoke interactive modules
8. Automated web scraping and data synchronisation mechanisms
9. News Page
10.Webinar facilities
11. Basic SEO optimisation
12. Speed and performance optimisation
13. Security configuration
14. Google Analytics integration
15. Cross-browser and mobile testing
16. Website deployment and launch support

Target Market(s)

My target markets are companies, investors, suppliers and professionals with an interest in the Mozambican oil and gas sector

Industry/Entity Type

Oil and Gas

Coding

Coded - Design and coding required

Number of Pages Required

1 page

Requirements
Must have
• Improve the existing page at https://quorin.net/tamberly and add the following features to it: 1. Search functionality 2. Payment process functionality 3. Application configuration 4. Activation of registration functionality 5. Chat functionality 6. Language switching functionality (Portuguese & French) 7. Bespoke interactive modules 8. Automated web scraping and data synchronisation mechanisms 9. News Page

```html
<!DOCTYPE html>
<html lang="en">
<head>
<meta charset="utf-8">
<title>Tamberly — Mozambique Oil &amp; Gas Intelligence</title>
<link rel="stylesheet" href="https://fonts.googleapis.com/css2?family=Outfit:wght@400;500;600&family=Inter:wght@400;500;600&display=swap">
<style>
:root{
  --navy:#0d2340;
  --navy-deep:#0b1a45;
  --orange:#ef8a32;
  --amber:#f6a62c;
  --ink:#141821;
  --muted:#5f6673;
  --beige:#f4f1ec;
  --line:#e6e2db;
  --white:#ffffff;
}
*{box-sizing:border-box;margin:0;padding:0}
html,body{width:1200px;height:4070px;overflow:hidden}
body{font-family:"Inter",sans-serif;color:var(--ink);background:var(--white);position:relative}
h1,h2,h3{font-family:"Outfit",sans-serif;font-weight:500;letter-spacing:-0.02em}
.abs{position:absolute}
.accent{color:var(--orange)}
.amber{color:var(--amber)}

/* nav */
.nav{top:0;left:0;width:1200px;height:85px;display:flex;align-items:center;padding:0 70px;background:var(--white)}
.brand{display:flex;align-items:center;gap:10px;font-family:"Outfit",sans-serif;font-weight:600;font-size:17px;color:var(--ink);letter-spacing:0.02em}
.brand-dot{width:26px;height:26px;border-radius:50%;background:var(--navy)}
.nav-links{display:flex;gap:18px;margin-left:42px;font-size:13px;font-weight:500}
.nav-links span{display:flex;align-items:center;gap:5px}
.nav-links .current{color:var(--orange)}
.nav-links .small{font-size:11.5px}
.nav-tools{margin-left:auto;display:flex;align-items:center;gap:10px}
.search-btn{width:32px;height:32px;border-radius:50%;border:1px solid var(--line);display:flex;align-items:center;justify-content:center}
.lang{display:flex;border:1px solid var(--line);border-radius:20px;font-size:10.5px;font-weight:600;overflow:hidden}
.lang span{padding:6px 7px;color:var(--muted)}
.lang .on{background:var(--navy);color:var(--white)}
.btn{display:inline-flex;align-items:center;justify-content:center;gap:7px;border-radius:30px;font-family:"Inter",sans-serif;font-weight:600;font-size:13px}
.btn-orange{background:var(--orange);color:var(--white)}
.btn-ghost{border:1px solid rgba(255,255,255,.35);color:var(--white)}
.nav .btn{width:104px;height:37px}

/* hero */
.hero{top:85px;left:0;width:1200px;height:707px;background:linear-gradient(180deg,#2f2a55 0%,#3b2f55 40%,#2a2237 70%,#1a1a22 100%)}
.hero-photo{position:absolute;inset:0;background:radial-gradient(ellipse 380px 420px at 890px 380px,rgba(190,200,60,.18),transparent 70%),linear-gradient(90deg,rgba(20,18,40,.55) 0%,rgba(20,18,40,0) 60%)}
.pill{display:inline-flex;align-items:center;gap:7px;border-radius:20px;font-size:10px;font-weight:500;padding:5px 11px}
.pill i{width:5px;height:5px;border-radius:50%;background:#47c26a;display:block}
.hero .pill{position:absolute;left:65px;top:88px;border:1px solid rgba(255,255,255,.25);color:#e8e6f0}
.hero h1{position:absolute;left:65px;top:135px;font-size:52px;line-height:63px;color:var(--white);width:600px}
.hero p{position:absolute;left:65px;top:360px;width:490px;font-size:13px;line-height:23px;color:#d9d6e2}
.hero .btn-orange{position:absolute;left:65px;top:463px;width:174px;height:50px}
.hero .btn-ghost{position:absolute;left:271px;top:463px;width:135px;height:50px}
.stats{position:absolute;left:65px;top:565px;display:flex}
.stat{width:149px;color:var(--white)}
.stat b{display:block;font-family:"Outfit",sans-serif;font-weight:500;font-size:25px}
.stat small{font-size:9.5px;letter-spacing:.08em;color:#b8b4c6}
.chat-btn{position:absolute;right:60px;bottom:40px;display:flex;align-items:center;gap:8px;height:46px;padding:0 18px;border-radius:30px;background:var(--orange);color:var(--white);font-size:13px;font-weight:600;box-shadow:0 6px 18px rgba(0,0,0,.3)}

/* news */
.news{left:65px;top:812px;width:1070px;height:44px;border:1px solid var(--line);border-radius:24px;display:flex;align-items:center;gap:18px;padding:0 8px;font-size:12.5px;color:var(--muted)}
.news-tag{background:var(--orange);color:var(--white);font-size:10px;font-weight:600;letter-spacing:.08em;border-radius:20px;padding:7px 12px}
.news-item{display:flex;align-items:center;gap:8px;white-space:nowrap}
.news-item b{color:var(--ink);font-weight:500}
.news-item i{width:4px;height:4px;border-radius:50%;background:var(--orange);display:block}
.news-more{margin-left:auto;color:var(--orange);font-weight:600;padding-right:10px}

/* about */
.about-pill{left:65px;top:899px;border:1px solid var(--line);color:var(--ink);font-weight:600;letter-spacing:.06em;font-size:9px}
.about-pill i{background:var(--orange)}
.about h2{left:65px;top:932px;font-size:42px;line-height:43px;width:560px}
.about p{left:65px;width:535px;font-size:13px;line-height:23.5px;color:var(--muted)}
.checks{left:65px;top:1265px;display:grid;grid-template-columns:272px 240px;row-gap:8px;font-size:15.5px;font-weight:500}
.checks span{display:flex;align-items:center;gap:8px}
.about-photo{left:636px;top:880px;width:503px;height:457px;border-radius:14px;background:linear-gradient(120deg,#1d2530 0%,#3a4756 45%,#6b7684 70%,#2a3441 100%)}

/* access */
.access{top:1425px;left:0;width:1200px;height:1070px;background:var(--beige)}
.ornament{left:430px;top:1490px;width:340px;height:44px}
.access-title{left:0;top:1547px;width:1200px;text-align:center;font-size:42px}
.card{width:339px;background:var(--white);border-radius:12px;padding:22px 20px;box-shadow:0 2px 8px rgba(0,0,0,.05)}
.icon{width:40px;height:40px;border-radius:10px;background:var(--navy);display:flex;align-items:center;justify-content:center}
.card h3{font-size:21px;line-height:24px;margin-top:24px;margin-bottom:16px}
.card p{font-size:12.5px;line-height:19px;color:var(--muted);width:260px}

/* how */
.how{left:50px;top:2391px;width:1086px;height:260px;border-radius:18px;background:radial-gradient(ellipse 900px 260px at 543px 330px,#2a4a7a 0%,#173155 50%,#0f2342 100%)}
.how h2{position:absolute;left:0;top:48px;width:100%;text-align:center;font-size:40px;color:var(--white)}
.how p{position:absolute;left:190px;top:118px;width:706px;text-align:center;font-size:12.5px;line-height:20px;color:#e2e8f2}
.pay{position:absolute;left:0;top:196px;width:100%;display:flex;justify-content:center;align-items:center;gap:14px;font-size:11.5px;color:#c9d3e4}
.pay .btn{height:36px;padding:0 18px;font-size:12px}

/* why */
.why h2{left:0;top:2735px;width:1200px;text-align:center;font-size:40px;color:var(--navy)}
.why-col{top:2830px;width:290px}
.why-icon{width:38px;height:38px;border-radius:10px;background:var(--amber);display:flex;align-items:center;justify-content:center}
.why-col h3{font-size:21px;line-height:26px;letter-spacing:.01em;margin:26px 0 18px;width:230px}
.why-col p{font-size:12.5px;line-height:16px;color:var(--muted)}
.divider{width:2px;height:185px;top:2835px;background:var(--orange);opacity:.7}

/* cta */
.cta{top:3111px;left:0;width:1200px;height:594px;background:radial-gradient(ellipse 700px 400px at 600px 300px,#142a66 0%,#0b1a45 70%,#091538 100%)}
.cta .pill{position:absolute;left:549px;top:135px;border:1px solid rgba(255,255,255,.3);color:#d7dcec;font-size:9px;letter-spacing:.1em}
.cta .pill i{background:var(--amber)}
.cta h2{position:absolute;left:0;top:190px;width:1200px;text-align:center;font-size:51px;line-height:58px;color:var(--white)}
.cta p{position:absolute;left:350px;top:335px;width:500px;text-align:center;font-size:13px;line-height:24px;color:#d7dcec}
.cta .btn-orange{position:absolute;left:438px;top:410px;width:164px;height:50px;font-size:12px}
.cta .btn-ghost{position:absolute;left:628px;top:410px;width:134px;height:50px;font-size:12px}

/* footer */
.foot-brand{left:0;top:3800px;width:1200px;display:flex;flex-direction:column;align-items:center;gap:12px;font-family:"Outfit",sans-serif;font-weight:600;font-size:16px}
.foot-links{left:0;top:3957px;width:1200px;display:flex;justify-content:center;gap:27px;font-size:13px;font-weight:500}
.foot-links .small{font-size:11.5px}
.copy{left:0;top:4038px;width:1200px;text-align:center;font-size:11px}
</style>
</head>
<body>

<header class="abs nav">
  <div class="brand"><span class="brand-dot"></span>TAMBERLY CO</div>
  <nav class="nav-links">
    <span class="current">Home</span>
    <span>Industry Insight <svg width="9" height="9" viewBox="0 0 10 10"><path d="M2 4l3 3 3-3" fill="none" stroke="#141821" stroke-width="1.4"/></svg></span>
    <span class="small">Oil &amp; Gas Opportunities <svg width="9" height="9" viewBox="0 0 10 10"><path d="M2 4l3 3 3-3" fill="none" stroke="#141821" stroke-width="1.4"/></svg></span>
    <span class="small">Supplier &amp; Compny Network <svg width="9" height="9" viewBox="0 0 10 10"><path d="M2 4l3 3 3-3" fill="none" stroke="#141821" stroke-width="1.4"/></svg></span>
    <span class="small">Legal Framework <svg width="9" height="9" viewBox="0 0 10 10"><path d="M2 4l3 3 3-3" fill="none" stroke="#141821" stroke-width="1.4"/></svg></span>
    <span class="small">News</span>
  </nav>
  <div class="nav-tools">
    <span class="search-btn" aria-label="Search"><svg width="14" height="14" viewBox="0 0 24 24" fill="none" stroke="#141821" stroke-width="2"><circle cx="11" cy="11" r="7"/><path d="M20 20l-4-4"/></svg></span>
    <div class="lang" aria-label="Language"><span class="on">EN</span><span>PT</span><span>FR</span></div>
    <a class="btn btn-orange">Register →</a>
  </div>
</header>

<section class="abs hero">
  <div class="hero-photo" role="img" aria-label="Two field engineers in high-visibility gear and hard hats inspecting a gas processing plant at dusk"></div>
  <span class="pill"><i></i>Mozambique Oil &amp; Gas Intelligence — Live</span>
  <h1>Access Mozambique’s <span class="amber">Oil &amp; Gas Industry</span> Intelligence in one platform.</h1>
  <p>Tamberly is a modern connection and consulting platform providing premium insights, supplier data, tenders, legal frameworks and strategic project intelligence for Mozambique’s hydrocarbons industry.</p>
  <a class="btn btn-orange">Register Now →</a>
  <a class="btn btn-ghost">Learn More</a>
  <div class="stats">
    <div class="stat"><b>1,200+</b><small>VERIFIED SUPPLIERS</small></div>
    <div class="stat"><b>48</b><small>ACTIVE TENDERS</small></div>
    <div class="stat"><b>9</b><small>FLAGSHIP PROJECTS</small></div>
  </div>
  <a class="chat-btn"><svg width="16" height="16" viewBox="0 0 24 24" fill="none" stroke="#fff" stroke-width="2"><path d="M4 5h16v11H9l-5 4z"/></svg>Chat with us</a>
</section>

<div class="abs news">
  <span class="news-tag">LATEST NEWS</span>
  <span class="news-item"><i></i><b>Offshore licensing round announced</b></span>
  <span class="news-item"><i></i><b>Local content rules updated</b></span>
  <span class="news-item"><i></i><b>Supplier pre-qualification window opens</b></span>
  <span class="news-more">All news →</span>
</div>

<section class="about">
  <span class="abs pill about-pill"><i></i>WHAT IS TAMBERLY</span>
  <h2 class="abs">One secure gateway to <span class="accent">Mozambique’s hydrocarbons</span> industry.</h2>
  <p class="abs" style="top:1088px">Tamberly is a unique online platform built to connect businesses, investors, suppliers and professionals with valuable information about the Mozambican Oil &amp; Gas sector.</p>
  <p class="abs" style="top:1148px">Through a secure digital paywall, users gain access to organized, up-to-date and carefully selected industry information — supporting better decisions, deeper market understanding and real business opportunities within Mozambique’s growing hydrocarbons industry.</p>
  <div class="abs checks">
    <span><svg width="15" height="15" viewBox="0 0 16 16"><circle cx="8" cy="8" r="6.5" fill="none" stroke="#ef8a32" stroke-width="1.3"/><path d="M5 8.2l2 2 4-4" fill="none" stroke="#ef8a32" stroke-width="1.3"/></svg>Curated by sector analysts</span>
    <span><svg width="15" height="15" viewBox="0 0 16 16"><circle cx="8" cy="8" r="6.5" fill="none" stroke="#ef8a32" stroke-width="1.3"/><path d="M5 8.2l2 2 4-4" fill="none" stroke="#ef8a32" stroke-width="1.3"/></svg>Verified supplier network</span>
    <span><svg width="15" height="15" viewBox="0 0 16 16"><circle cx="8" cy="8" r="6.5" fill="none" stroke="#ef8a32" stroke-width="1.3"/><path d="M5 8.2l2 2 4-4" fill="none" stroke="#ef8a32" stroke-width="1.3"/></svg>Tender-ready playbooks</span>
    <span><svg width="15" height="15" viewBox="0 0 16 16"><circle cx="8" cy="8" r="6.5" fill="none" stroke="#ef8a32" stroke-width="1.3"/><path d="M5 8.2l2 2 4-4" fill="none" stroke="#ef8a32" stroke-width="1.3"/></svg>Secure paywall access</span>
  </div>
  <div class="abs about-photo" role="img" aria-label="Two businessmen in suits walking through an office corridor reviewing a document"></div>
</section>

<section class="abs access"></section>
<svg class="abs ornament" viewBox="0 0 340 44"><line x1="0" y1="22" x2="140" y2="22" stroke="#ef8a32" stroke-width="1.2"/><line x1="200" y1="22" x2="340" y2="22" stroke="#ef8a32" stroke-width="1.2"/><circle cx="170" cy="22" r="9" fill="#0d2340"/></svg>
<h2 class="abs access-title">What You <span class="accent">Will Access</span></h2>

<div class="abs card" style="left:66px;top:1658px;height:215px"><div class="icon"><svg width="18" height="18" viewBox="0 0 24 24" fill="none" stroke="#fff" stroke-width="1.8"><rect x="4" y="4" width="10" height="16" rx="1"/><path d="M14 9h3l2 3v6h-3"/></svg></div><h3>Hydrocarbon Industry Intelligence</h3><p>General information and insights about Mozambique’s oil and gas sector.</p></div>
<div class="abs card" style="left:430px;top:1658px;height:215px"><div class="icon"><svg width="18" height="18" viewBox="0 0 24 24" fill="none" stroke="#fff" stroke-width="1.8"><path d="M4 16a8 8 0 0116 0"/><path d="M12 16l4-5"/></svg></div><h3>Main Gas Projects</h3><p>Details about major gas and energy projects operating in Mozambique.</p></div>
<div class="abs card" style="left:795px;top:1658px;height:215px"><div class="icon"><svg width="18" height="18" viewBox="0 0 24 24" fill="none" stroke="#fff" stroke-width="1.8"><ellipse cx="12" cy="6" rx="7" ry="3"/><path d="M5 6v12c0 1.7 3 3 7 3s7-1.3 7-3V6M5 12c0 1.7 3 3 7 3s7-1.3 7-3"/></svg></div><h3>Supplier &amp; Company Database</h3><p>Mozambican companies capable of meeting Level 3 supply requirements.</p></div>

<div class="abs card" style="left:66px;top:1892px;height:196px"><div class="icon"><svg width="18" height="18" viewBox="0 0 24 24" fill="none" stroke="#fff" stroke-width="1.8"><circle cx="9" cy="8" r="3.5"/><path d="M2 20c0-4 3-6 7-6s7 2 7 6M16 4.5a3.5 3.5 0 010 7M19 14c2 1 3 3 3 6"/></svg></div><h3>Industry Contacts</h3><p>Key contacts from NOCs, Operators, EPCs, and Second-Tier Suppliers.</p></div>
<div class="abs card" style="left:430px;top:1892px;height:196px"><div class="icon"><svg width="18" height="18" viewBox="0 0 24 24" fill="none" stroke="#fff" stroke-width="1.8"><path d="M6 3h8l4 4v14H6z"/><path d="M9 12h6M9 16h6"/></svg></div><h3>Tender Opportunities</h3><p>Short, medium, and long-term tenders within the industry.</p></div>
<div class="abs card" style="left:795px;top:1892px;height:196px"><div class="icon"><svg width="18" height="18" viewBox="0 0 24 24" fill="none" stroke="#fff" stroke-width="1.8"><path d="M12 3l7 3v6c0 4-3 7-7 9-4-2-7-5-7-9V6z"/><path d="M9 12l2 2 4-4"/></svg></div><h3>Ownership &amp; Access</h3><p>Understand the concession map, block ownership, and operator responsibilities at a glance.</p></div>

<div class="abs card" style="left:66px;top:2106px;height:196px"><div class="icon"><svg width="18" height="18" viewBox="0 0 24 24" fill="none" stroke="#fff" stroke-width="1.8"><path d="M12 4v16M6 20h12M4 8h16M4 8l-2 6h4zM20 8l-2 6h4z"/></svg></div><h3>Legal Framework</h3><p>Petroleum laws, fiscal regime, local content rules and compliance updates in one place.</p></div>
<div class="abs card" style="left:430px;top:2106px;height:196px"><div class="icon"><svg width="18" height="18" viewBox="0 0 24 24" fill="none" stroke="#fff" stroke-width="1.8"><rect x="5" y="3" width="14" height="18" rx="1"/><path d="M9 7h2M13 7h2M9 11h2M13 11h2M10 21v-4h4v4"/></svg></div><h3>Local Company Capacity</h3><p>Assess Mozambican SME capacity, certifications, and readiness for major project engagement.</p></div>
<div class="abs card" style="left:795px;top:2106px;height:196px"><div class="icon"><svg width="18" height="18" viewBox="0 0 24 24" fill="none" stroke="#fff" stroke-width="1.8"><circle cx="12" cy="12" r="8"/><path d="M8 12l3 3 5-6"/></svg></div><h3>Tender Application Guidance</h3><p>Structured playbooks, checklists and templates to submit competitive, compliant bids.</p></div>

<section class="abs how" role="img" aria-label="Night view of the Earth with glowing network lines">
  <h2>How <span class="amber">the platform</span> works.</h2>
  <p>The platform operates through a secure automated payment system that grants registered users access to premium and exclusive content. By subscribing, users receive organized industry intelligence designed to save time, improve market access, and support strategic business growth within Mozambique’s energy sector.</p>
  <div class="pay">
    <a class="btn btn-orange"><svg width="13" height="13" viewBox="0 0 24 24" fill="none" stroke="#fff" stroke-width="2"><rect x="5" y="11" width="14" height="10" rx="2"/><path d="M8 11V7a4 4 0 018 0v4"/></svg>Subscribe &amp; Pay Securely</a>
    <span>Monthly or annual plans · Encrypted checkout</span>
  </div>
</section>

<section class="why">
  <h2 class="abs">Why Tamberly Is Unique</h2>
  <div class="abs why-col" style="left:89px"><div class="why-icon"><svg width="17" height="17" viewBox="0 0 24 24" fill="none" stroke="#0d2340" stroke-width="1.8"><rect x="4" y="4" width="10" height="16" rx="1"/><path d="M14 9h3l2 3v6h-3"/></svg></div><h3>Up-To-Date Industry Intelligence</h3><p>Receive frequent updates about developments in Mozambique’s Oil &amp; Gas sector.</p></div>
  <div class="abs divider" style="left:397px"></div>
  <div class="abs why-col" style="left:444px;top:2840px"><div class="why-icon"><svg width="17" height="17" viewBox="0 0 24 24" fill="none" stroke="#0d2340" stroke-width="1.8"><rect x="4" y="4" width="10" height="16" rx="1"/><path d="M14 9h3l2 3v6h-3"/></svg></div><h3>High-Quality Curated Information</h3><p>Access carefully selected and synthesized information tailored to industry stakeholders.</p></div>
  <div class="abs divider" style="left:778px"></div>
  <div class="abs why-col" style="left:824px"><div class="why-icon"><svg width="17" height="17" viewBox="0 0 24 24" fill="none" stroke="#0d2340" stroke-width="1.8"><rect x="4" y="4" width="10" height="16" rx="1"/><path d="M14 9h3l2 3v6h-3"/></svg></div><h3 style="width:150px">Time-Saving Access</h3><p>Avoid spending hours searching through scattered online sources with organized and accessible content in one platform.</p></div>
</section>

<section class="abs cta">
  <span class="pill"><i></i>GET STARTED</span>
  <h2>Start exploring Mozambique’s<br><span class="amber">Oil &amp; Gas opportunities</span></h2>
  <p>Register today to access premium industry information, supplier networks, tenders, and strategic market insights through Tamberly.</p>
  <a class="btn btn-orange">Register Now →</a>
  <a class="btn btn-ghost">Contact Us</a>
</section>

<footer>
  <div class="abs foot-brand"><span class="brand-dot" style="width:40px;height:40px"></span>TAMBERLY CO</div>
  <nav class="abs foot-links">
    <span>Home</span><span>Industry Insight</span><span class="small">Oil &amp; Gas Opportunities</span><span class="small">Supplier &amp; Compny Network</span><span class="small">Legal Framework</span><span class="small">News</span>
  </nav>
  <p class="abs copy">© 2026 by Tamberly Co. All Rights Reserved</p>
</footer>

</body>
</html>
```